I need a two page flyer (one page front and back) outlining our residential furniture rental options.

Title: Premium Residential Furniture Rentals

GOOD
Our Bellmore Ridge Furniture Package is designed to offer a perfect balance of affordability and style, without compromising on quality. This package features a selection of functional and aesthetically pleasing furniture pieces, ideal for those looking to create a polished and professional space. With quick installation handled by our experienced in-house team, you can expect a smooth and hassle-free setup. This package ensures both convenience and value, providing a streamlined solution for your needs.
Living room, dining room and bedroom (additional bedrooms available)
- $710/month with a 3 month commitment
- $570/month with a 6 month commitment

BETTER
Our Premium Furniture Package takes comfort and style to the next level, offering an enhanced experience compared to our Bellmore option. Carefully selected with durability in mind, this package features high-quality, convenient furniture designed for both functionality and aesthetics. Perfect for those seeking a more refined look and superior comfort, it’s ideal for creating a sophisticated and inviting environment. With attention to detail in both design and craftsmanship, the premium package elevates any space, ensuring a higher standard of comfort and style that caters to both employees and clients.
- $1,150/month with a 3 month commitment
- $900/month with a 6 month commitment

BEST
Our Custom Furniture Package offers a tailored experience where you’ll work directly with our expert designer to create the ultimate luxurious and functional space. We include lounging, dining, sleeping and working from home, this package allows you to curate a space that perfectly fits your needs and style. With personalized attention to detail, we ensure every element is designed to provide the highest level of comfort, convenience, and elegance, transforming your space into a sophisticated sanctuary for relaxation and enjoyment.
Please inquire for pricing

www.quillbyhomeleasing.example

```html
<!DOCTYPE html>
<html lang="en">
<head>
<meta charset="utf-8">
<title>Premium Residential Furniture Rentals – Flyer</title>
<link href="https://fonts.googleapis.com/css2?family=Montserrat:wght@400;500;600;700;800;900&display=swap" rel="stylesheet">
<style>
:root{
  --navy:#1f2a5c;
  --yellow:#d9bd2a;
  --white:#ffffff;
  --stage:#6f6f71;
  --body:#6b6b70;
  --muted:#8b93b8;
}
*{margin:0;padding:0;box-sizing:border-box}
html,body{width:1200px;height:2967px;overflow:hidden}
body{background:var(--stage);font-family:"Montserrat",sans-serif;position:relative}
.page{position:absolute;left:220px;width:760px;height:1076px;overflow:hidden}
.page-front{top:357px}
.page-back{top:1533px;background:var(--white)}

/* front */
.room-photo{position:absolute;inset:0;background:linear-gradient(160deg,#e9e4dc 0%,#cfc7b8 40%,#b9ad98 65%,#5b5a58 100%)}
.frame{position:absolute;left:36px;right:36px;top:38px;bottom:35px;border:4px solid var(--white)}
.brand-box{position:absolute;left:249px;top:0;width:264px;height:194px;background:var(--navy);color:var(--white);text-align:center;padding-top:88px}
.brand-name{font-size:19px;font-weight:500;letter-spacing:.5px}
.brand-sub{display:flex;align-items:center;justify-content:center;gap:10px;font-size:10px;letter-spacing:9px;margin-top:6px}
.brand-sub::before,.brand-sub::after{content:"";width:28px;height:1px;background:var(--white)}
.brand-tags{font-size:7.5px;font-weight:600;letter-spacing:.4px;margin-top:7px}
.title-band{position:absolute;left:41px;right:41px;top:904px;height:138px;background:var(--yellow);display:flex;align-items:center;justify-content:center;text-align:center}
.title-band h1{color:var(--white);font-size:38px;font-weight:800;line-height:1.12;letter-spacing:.6px}

/* back */
.tier{position:absolute;left:57px;width:646px;border:3px solid var(--navy)}
.tier-good{top:45px;height:279px}
.tier-better{top:354px;height:283px}
.tier-best{top:664px;height:277px}
.tier h2{position:absolute;left:31px;top:8px;color:var(--navy);font-size:36px;font-weight:800;letter-spacing:.5px}
.tier-copy{position:absolute;left:31px;top:62px;width:326px;font-size:9.6px;line-height:1.55;color:var(--body);text-align:justify}
.tier-best .tier-copy{width:550px}
.tier-rooms{position:absolute;left:31px;font-size:9px;font-weight:700;color:#333;line-height:1.3}
.tier-rooms small{display:block;font-weight:400;font-size:8px;color:var(--body)}
.tier-good .tier-rooms{top:228px}
.tier-better .tier-rooms{top:232px}
.price-panel{position:absolute;left:370px;width:242px;background:var(--navy);padding:0 32px}
.tier-good .price-panel{top:26px;height:224px}
.tier-better .price-panel{top:26px;height:226px}
.price{display:flex;align-items:flex-end;gap:4px;font-weight:800;font-size:38px;line-height:1;letter-spacing:-1px}
.price-3{color:var(--yellow);padding-top:30px}
.price-6{color:var(--white)}
.per{font-size:13px;font-weight:700;font-style:italic;letter-spacing:0;padding:2px 10px 2px 6px;margin-bottom:5px;clip-path:polygon(6% 0,100% 0,94% 100%,0 100%)}
.price-3 .per{background:var(--white);color:var(--navy)}
.price-6 .per{background:var(--yellow);color:var(--navy)}
.term{font-size:9px;color:var(--muted);margin-top:8px}
.term-3 b{color:var(--white)}
.term-6 b{color:var(--yellow)}
.divider{height:2px;background:var(--yellow);margin:22px 0 26px}
.inquire-bar{position:absolute;left:31px;top:160px;width:552px;height:45px;display:flex}
.inquire{width:253px;background:var(--yellow);color:var(--navy);font-size:11px;font-weight:600;display:flex;align-items:center;justify-content:center}
.web{flex:1;background:var(--navy);color:var(--white);font-size:13px;display:flex;align-items:center;gap:12px;padding-left:0}
.web svg{margin-left:-14px;background:var(--white);border-radius:50%}
.web b{font-weight:700}
.footer{position:absolute;left:0;right:0;top:943px;height:133px;background:var(--yellow);color:var(--white);text-align:center;padding-top:14px}
.footer-title{font-size:19px;font-weight:500;letter-spacing:.5px}
.footer-address{font-size:13px;margin-top:4px;display:flex;align-items:center;justify-content:center;gap:5px}
.footer-phone{font-size:33px;font-weight:800;color:var(--navy);margin-top:6px;display:flex;align-items:center;justify-content:center;gap:6px}
.footer-phone svg{fill:var(--white)}
</style>
</head>
<body>

<section class="page page-front">
  <div class="room-photo" role="img" aria-label="Furnished living room with a cream tufted sofa, armchair, round coffee tables, patterned rug and abstract wall art"></div>
  <div class="frame"></div>
  <div class="brand-box">
    <div class="brand-name">QUILLBY HOME</div>
    <div class="brand-sub">LEASING</div>
    <div class="brand-tags">STAGING | RESIDENTIAL | CORPORATE | SALES</div>
  </div>
  <div class="title-band"><h1>PREMIUM RESIDENTIAL<br>FURNITURE RENTALS</h1></div>
</section>

<section class="page page-back">
  <article class="tier tier-good">
    <h2>GOOD</h2>
    <p class="tier-copy">Our Bellmore Ridge Furniture Package is designed to offer a perfect balance of affordability and style, without compromising on quality. This package features a selection of functional and aesthetically pleasing furniture pieces, ideal for those looking to create a polished and professional space. With quick installation handled by our experienced in-house team, you can expect a smooth and hassle-free setup. This package ensures both convenience and value, providing a streamlined solution for your needs.</p>
    <p class="tier-rooms">Living room, dining room and bedroom<small>(additional bedrooms available)</small></p>
    <div class="price-panel">
      <div class="price price-3">$710<span class="per">/month</span></div>
      <p class="term term-3">with a <b>3 month</b> commitment</p>
      <div class="divider"></div>
      <div class="price price-6">$570<span class="per">/month</span></div>
      <p class="term term-6">with a <b>6 month</b> commitment</p>
    </div>
  </article>

  <article class="tier tier-better">
    <h2>BETTER</h2>
    <p class="tier-copy">Our Premium Furniture Package takes comfort and style to the next level, offering an enhanced experience compared to our Bellmore option. Carefully selected with durability in mind, this package features high-quality, convenient furniture designed for both functionality and aesthetics. Perfect for those seeking a more refined look and superior comfort, it’s ideal for creating a sophisticated and inviting environment. With attention to detail in both design and craftsmanship, the premium package elevates any space, ensuring a higher standard of comfort and style that caters to both employees and clients.</p>
    <p class="tier-rooms">Living room, dining room and bedroom<small>(additional bedrooms available)</small></p>
    <div class="price-panel">
      <div class="price price-3">$1,150<span class="per">/month</span></div>
      <p class="term term-3">with a <b>3 month</b> commitment</p>
      <div class="divider"></div>
      <div class="price price-6">$900<span class="per">/month</span></div>
      <p class="term term-6">with a <b>6 month</b> commitment</p>
    </div>
  </article>

  <article class="tier tier-best">
    <h2>BEST</h2>
    <p class="tier-copy">Our Custom Furniture Package offers a tailored experience where you’ll work directly with our expert designer to create the ultimate luxurious and functional space. We include lounging, dining, sleeping and working from home, this package allows you to curate a space that perfectly fits your needs and style. With personalized attention to detail, we ensure every element is designed to provide the highest level of comfort, convenience, and elegance, transforming your space into a sophisticated sanctuary for relaxation and enjoyment.</p>
    <div class="inquire-bar">
      <div class="inquire">PLEASE INQUIRE FOR PRICING</div>
      <div class="web">
        <svg width="26" height="26" viewBox="0 0 26 26" aria-hidden="true"><g fill="none" stroke="#1f2a5c" stroke-width="1.4"><circle cx="13" cy="13" r="9"/><ellipse cx="13" cy="13" rx="4" ry="9"/><path d="M4 13h18M5.5 8.5h15M5.5 17.5h15"/></g></svg>
        <span>www.<b>quillbyhomeleasing</b>.example</span>
      </div>
    </div>
  </article>

  <footer class="footer">
    <p class="footer-title">RESIDENTIAL FURNITURE RENTAL</p>
    <p class="footer-address">
      <svg width="10" height="13" viewBox="0 0 10 13" aria-hidden="true"><path fill="#fff" d="M5 0a5 5 0 0 0-5 5c0 3.5 5 8 5 8s5-4.5 5-8a5 5 0 0 0-5-5zm0 7a2 2 0 1 1 0-4 2 2 0 0 1 0 4z"/></svg>
      1420 Alder Court #12, Springfield, Ohio 45501, United States
    </p>
    <p class="footer-phone">
      <svg width="22" height="22" viewBox="0 0 24 24" aria-hidden="true"><path d="M6.6 10.8a15.1 15.1 0 0 0 6.6 6.6l2.2-2.2c.3-.3.7-.4 1-.2 1.1.4 2.3.6 3.6.6.6 0 1 .4 1 1V20c0 .6-.4 1-1 1C10.6 21 3 13.4 3 4c0-.6.4-1 1-1h3.5c.6 0 1 .4 1 1 0 1.3.2 2.5.6 3.6.1.3 0 .7-.2 1l-2.3 2.2z"/></svg>
      555-014-2290
    </p>
  </footer>
</section>

</body>
</html>
```